Merrowind Flyer

A simple flyer that gets people attention
I have a attached a sample of what we use now and a picture we use
We service gas fireplaces and need a eye catching but not to cluttered flyer to promote our business. the cost per fireplace should be $60.00

Reason: Sorry for the delay We are out of town on holidays with sketchy internet service To frustrating to complete this project till I am back in a week Thank you for your patience Kind regards Dale

```html
<!DOCTYPE html>
<html lang="en">
<head>
<meta charset="utf-8">
<title>Merrowind Gas Services Flyer</title>
<link rel="stylesheet" href="https://fonts.googleapis.com/css2?family=Creepster&family=Archivo:wght@700;800&display=swap">
<style>
  :root {
    --tile: #8f8f8f;
    --tile-light: #a3a3a3;
    --grout: #e4e4e4;
    --ink: #0c0c0c;
    --flame-hot: #ffd23a;
    --flame-mid: #f07a12;
    --flame-deep: #8a1a05;
    --glow: #d8361a;
    --frame: #1a0a08;
  }
  html, body { margin: 0; padding: 0; overflow: hidden; }
  body { width: 928px; height: 1200px; }
  .flyer {
    position: relative;
    width: 928px;
    height: 1200px;
    overflow: hidden;
    background: radial-gradient(ellipse at 40% 45%, var(--tile-light), var(--tile) 70%);
    font-family: "Archivo", Arial, sans-serif;
    color: var(--ink);
  }
  .tile-grid { position: absolute; inset: 0; }
  .headline {
    position: absolute;
    top: 40px; left: 0; width: 100%;
    margin: 0;
    text-align: center;
    font-family: "Creepster", fantasy;
    font-weight: 400;
    font-size: 104px;
    letter-spacing: 2px;
    line-height: 1;
    background: linear-gradient(180deg, var(--flame-hot) 15%, var(--flame-mid) 55%, var(--flame-deep) 95%);
    -webkit-background-clip: text;
    background-clip: text;
    color: transparent;
    filter: drop-shadow(3px 4px 2px rgba(0,0,0,0.7));
  }
  .fireplace-photo {
    position: absolute;
    left: 114px; top: 298px;
    width: 702px; height: 432px;
    background:
      radial-gradient(ellipse 40% 36% at 49% 62%, #ffb23a, #f06a14 45%, #c2360c 75%, transparent 100%),
      linear-gradient(180deg, #2a0c08, var(--frame));
    box-shadow: 0 4px 10px rgba(0,0,0,0.35);
  }
  .price {
    position: absolute;
    top: 790px; left: 0; width: 100%;
    margin: 0;
    text-align: center;
    font-weight: 800;
    font-size: 62px;
    letter-spacing: -0.5px;
    text-shadow: 0 0 8px var(--glow), 0 0 16px var(--glow), 0 0 4px var(--glow);
  }
  .contact {
    position: absolute;
    top: 946px; left: 0; width: 100%;
    margin: 0;
    text-align: center;
    font-weight: 700;
    font-size: 32px;
    line-height: 1.8;
  }
  .email {
    position: absolute;
    top: 1108px; left: 0; width: 100%;
    margin: 0;
    text-align: center;
    font-weight: 700;
    font-size: 30px;
  }
</style>
</head>
<body>
  <main class="flyer">
    <svg class="tile-grid" width="928" height="1200" viewBox="0 0 928 1200" aria-hidden="true">
      <g stroke="var(--grout)" stroke-width="3">
        <line x1="164" y1="0" x2="164" y2="1200"/>
        <line x1="744" y1="0" x2="744" y2="1200"/>
        <line x1="0" y1="126" x2="928" y2="126"/>
        <line x1="0" y1="420" x2="928" y2="420"/>
        <line x1="0" y1="714" x2="928" y2="714"/>
        <line x1="0" y1="1006" x2="928" y2="1006"/>
      </g>
    </svg>

    <h1 class="headline">MERROWIND GAS SERVICES</h1>

    <div class="fireplace-photo" role="img" aria-label="Modern gas fireplace insert with a dark frame and glowing flames over ceramic logs"></div>

    <p class="price">The cost&nbsp; per fireplace is $60.00</p>

    <p class="contact">For further information please contact Maren at:<br>555.014.2290</p>

    <p class="email">email us at: maren.merrowindgas@mailbox.example</p>
  </main>
</body>
</html>
```